Animal Puzzle game Needs Design

Need a redesign of the UI of this puzzle game and a forest background. This game is for any age. The design needs to be on separate layers in Photoshop. The design needs to be colorful and easy to see the different UI parts, sound control, progress bar, number of lives and number of moves.

Target Market(s)

All ages

Requirements
Must have
• Needs to have each of the UI elements and a background.

```html
<!DOCTYPE html>
<html lang="en">
<head>
<meta charset="utf-8">
<title>Forest Puzzle – Level 1</title>
<link href="https://fonts.googleapis.com/css2?family=PT+Sans+Narrow:wght@400;700&display=swap" rel="stylesheet">
<style>
  :root {
    --forest-deep: #0f2a03;
    --forest-mid: #3f8a0c;
    --forest-bright: #8fd12a;
    --forest-glow: #e6f9b8;
    --lime: #c9ef5a;
    --lime-pale: #e4f8b0;
    --tile-edge: #2c5508;
    --panel-dark: #1e3a06;
    --white: #ffffff;
    --track: #1a1a14;
    --ink-dark: #1d3303;
  }
  * { margin: 0; padding: 0; box-sizing: border-box; }
  html, body { width: 1200px; height: 1039px; overflow: hidden; background: var(--forest-deep); }
  body { font-family: "PT Sans Narrow", "Arial Narrow", sans-serif; }

  .game-screen { position: relative; width: 1200px; height: 1039px; overflow: hidden; }

  .forest-background {
    position: absolute; inset: 0;
    background:
      radial-gradient(ellipse 330px 260px at 110px 300px, var(--forest-glow) 0%, rgba(230,249,184,0.6) 35%, rgba(230,249,184,0) 75%),
      radial-gradient(ellipse 520px 360px at 420px 120px, rgba(200,240,110,0.75) 0%, rgba(200,240,110,0) 80%),
      radial-gradient(ellipse 500px 500px at 1050px 360px, rgba(120,200,30,0.7) 0%, rgba(120,200,30,0) 75%),
      linear-gradient(180deg, rgba(15,42,3,0) 55%, rgba(15,42,3,0.85) 100%),
      linear-gradient(100deg, var(--forest-bright) 0%, var(--forest-mid) 45%, #2f6e08 75%, #1c4a04 100%);
  }

  /* Lives */
  .lives-badge { position: absolute; left: 57px; top: 74px; width: 124px; height: 112px; }
  .lives-badge svg { position: absolute; inset: 0; }
  .lives-badge .label {
    position: absolute; left: 0; right: 0; top: 34px; text-align: center;
    font-size: 26px; color: var(--ink-dark);
  }

  /* Level */
  .level-panel {
    position: absolute; left: 500px; top: 75px; width: 242px; height: 100px;
    background: var(--panel-dark); border: 5px solid var(--white); border-radius: 3px;
    display: flex; align-items: baseline; justify-content: center; gap: 8px;
    padding-top: 20px; color: var(--lime);
  }
  .level-panel .word { font-size: 27px; }
  .level-panel .number { font-size: 54px; font-weight: 700; line-height: 1; }

  /* Moves */
  .moves-badge { position: absolute; left: 986px; top: 62px; width: 148px; height: 148px; }
  .moves-badge svg { position: absolute; inset: 0; }
  .moves-badge .label {
    position: absolute; left: 0; right: 0; top: 56px; text-align: center;
    font-size: 26px; color: var(--ink-dark);
  }

  /* Puzzle grid */
  .puzzle-grid {
    position: absolute; left: 259px; top: 227px;
    display: grid; grid-template-columns: repeat(5, 134px); grid-auto-rows: 134px;
    column-gap: 8px; row-gap: 8px;
  }
  .puzzle-tile {
    background: var(--tile-edge); padding: 5px; border-radius: 3px;
    box-shadow: 0 0 6px rgba(10,30,0,0.5);
  }
  .puzzle-tile .face {
    width: 100%; height: 100%; background: var(--lime-pale);
    border: 8px solid var(--white);
  }

  /* Progress */
  .progress-bar {
    position: absolute; left: 218px; top: 867px; width: 785px; height: 64px;
    border-radius: 32px;
    background: linear-gradient(180deg, #e4f56a 0%, #a8d41e 40%, #4f8a0a 100%);
    box-shadow: 0 2px 6px rgba(0,0,0,0.45);
  }
  .progress-track {
    position: absolute; left: 46px; top: 24px; width: 595px; height: 17px;
    background: var(--track); border-radius: 3px; padding: 3px;
  }
  .progress-fill { width: 46%; height: 100%; background: linear-gradient(180deg, #eefa8a, #c6e636); }
  .progress-time {
    position: absolute; left: 680px; top: 16px; font-size: 24px; color: var(--ink-dark);
  }

  /* Sound */
  .sound-toggle { position: absolute; left: 1030px; top: 855px; width: 94px; height: 88px; }
</style>
</head>
<body>
<main class="game-screen">
  <div class="forest-background" role="img" aria-label="Sunlit green forest with tree branches, leaves and swirling vines"></div>

  <div class="lives-badge">
    <svg viewBox="0 0 124 112" aria-hidden="true">
      <path d="M62 110 C40 92 2 70 2 36 C2 14 18 2 36 2 C48 2 57 9 62 18 C67 9 76 2 88 2 C106 2 122 14 122 36 C122 70 84 92 62 110 Z" fill="#c9ef5a"/>
    </svg>
    <span class="label">Lives</span>
  </div>

  <div class="level-panel">
    <span class="word">Lavel</span><span class="number">1</span>
  </div>

  <div class="moves-badge">
    <svg viewBox="0 0 148 148" aria-hidden="true">
      <g fill="#c9ef5a">
        <polygon points="74,10 90,46 130,42 106,74 130,106 90,102 74,138 58,102 18,106 42,74 18,42 58,46"/>
        <circle cx="74" cy="10" r="8"/><circle cx="130" cy="42" r="8"/><circle cx="130" cy="106" r="8"/>
        <circle cx="74" cy="138" r="8"/><circle cx="18" cy="106" r="8"/><circle cx="18" cy="42" r="8"/>
      </g>
    </svg>
    <span class="label">Movies</span>
  </div>

  <section class="puzzle-grid" aria-label="Puzzle tiles">
    <div class="puzzle-tile"><div class="face"></div></div>
    <div class="puzzle-tile"><div class="face"></div></div>
    <div class="puzzle-tile"><div class="face"></div></div>
    <div class="puzzle-tile"><div class="face"></div></div>
    <div class="puzzle-tile"><div class="face"></div></div>
    <div class="puzzle-tile"><div class="face"></div></div>
    <div class="puzzle-tile"><div class="face"></div></div>
    <div class="puzzle-tile"><div class="face"></div></div>
    <div class="puzzle-tile"><div class="face"></div></div>
    <div class="puzzle-tile"><div class="face"></div></div>
    <div class="puzzle-tile"><div class="face"></div></div>
    <div class="puzzle-tile"><div class="face"></div></div>
    <div class="puzzle-tile"><div class="face"></div></div>
    <div class="puzzle-tile"><div class="face"></div></div>
    <div class="puzzle-tile"><div class="face"></div></div>
    <div class="puzzle-tile"><div class="face"></div></div>
    <div class="puzzle-tile"><div class="face"></div></div>
    <div class="puzzle-tile"><div class="face"></div></div>
    <div class="puzzle-tile"><div class="face"></div></div>
    <div class="puzzle-tile"><div class="face"></div></div>
  </section>

  <div class="progress-bar">
    <div class="progress-track"><div class="progress-fill"></div></div>
    <span class="progress-time">40:00</span>
  </div>

  <svg class="sound-toggle" viewBox="0 0 94 88" aria-label="Sound on">
    <g fill="none" stroke="#ffffff" stroke-width="6" stroke-linejoin="round" stroke-linecap="round">
      <path d="M4 30 H18 L38 10 V78 L18 58 H4 Z"/>
      <path d="M50 30 Q58 44 50 58"/>
      <path d="M62 20 Q76 44 62 68"/>
      <path d="M74 10 Q94 44 74 78"/>
    </g>
  </svg>
</main>
</body>
</html>
```